Vela Luxe Gel Top Coat & Base Coat Box Design

We are a wholesale nail and beauty supply company located in the USA. We need an attractive box design for our product, Vela Luxe Gel Top Coat and Base Coat, to boost our sales to retail nail salons in the USA.
Dimension of the box is 11'' wide by 8.25'' long.
Color of the box is black with ingrained pattern (see picture).
Need design for top of box only.

Target Market(s)

Retail Nail Salons in the USA

Industry/Entity Type

Beauty Salon

Colors

Designer to choose colors to be used in the design.

Requirements
Must have
• Luxe Vela Gel Top Coat Base Coat
• Matching Font of our product label (see picture)
Nice to have
• Luxe should stand out.
• Line separating design for Top Coat and Base Coat (as they are 2 different products in the same box). Open to all color schemes, but would like to see some in silver.

```html
<!DOCTYPE html>
<html lang="en">
<head>
<meta charset="utf-8">
<title>Vela Luxe Gel Top Coat &amp; Base Coat – Box Lid</title>
<link rel="stylesheet" href="https://fonts.googleapis.com/css2?family=Montserrat:wght@700&family=Questrial&display=swap">
<style>
  :root {
    --lid: #120205;
    --silver: #c9c9cb;
    --silver-light: #f2f2f3;
    --silver-dark: #7d7d80;
    --text-soft: #e4e4e6;
  }
  html, body {
    margin: 0;
    width: 1200px;
    height: 1200px;
    overflow: hidden;
    background: var(--lid);
  }
  .lid {
    position: relative;
    width: 1200px;
    height: 1200px;
    background: var(--lid);
    font-family: "Questrial", sans-serif;
    color: var(--text-soft);
  }
  .lid svg.rules {
    position: absolute;
    inset: 0;
  }
  .brand-mark {
    position: absolute;
    width: 300px;
    height: 300px;
    display: flex;
    align-items: center;
    justify-content: center;
    box-sizing: border-box;
    border: 3px solid var(--silver);
    border-radius: 50%;
    font-family: "Questrial", sans-serif;
    font-size: 58px;
    letter-spacing: 6px;
    color: var(--silver);
  }
  .brand-mark--top { left: 198px; top: 203px; }
  .brand-mark--bottom { left: 738px; top: 738px; }

  .title {
    position: absolute;
    width: 560px;
    text-align: center;
  }
  .title--top { left: 576px; top: 180px; }
  .title--bottom { left: 60px; top: 830px; }

  .title__main {
    display: flex;
    align-items: center;
    justify-content: space-between;
    padding: 0 18px;
    height: 90px;
  }
  .title__star {
    color: var(--silver);
    font-size: 38px;
    line-height: 1;
  }
  .title__word {
    font-family: "Montserrat", sans-serif;
    font-weight: 700;
    font-size: 76px;
    letter-spacing: 10px;
    line-height: 1;
    background: linear-gradient(90deg, var(--silver-dark), var(--silver-light) 45%, var(--silver) 70%, var(--silver-dark));
    -webkit-background-clip: text;
    background-clip: text;
    color: transparent;
  }
  .title__sub {
    font-size: 40px;
    letter-spacing: 2px;
    color: var(--silver);
    margin-top: 2px;
  }
  .coat-name {
    position: absolute;
    width: 560px;
    text-align: center;
    font-size: 62px;
    color: var(--text-soft);
  }
  .coat-name--top { left: 576px; top: 355px; }
  .coat-name--bottom { left: 60px; top: 985px; }
</style>
</head>
<body>
<main class="lid">
  <svg class="rules" width="1200" height="1200" viewBox="0 0 1200 1200" aria-hidden="true">
    <defs>
      <linearGradient id="band-silver" x1="0" x2="1" y1="0" y2="0">
        <stop offset="0" stop-color="#b8b8ba"/>
        <stop offset="0.5" stop-color="#fafafa"/>
        <stop offset="0.75" stop-color="#a9a9ac"/>
        <stop offset="1" stop-color="#6f6f72"/>
      </linearGradient>
    </defs>
    <!-- top hanging lines -->
    <g class="hanging-lines" stroke="var(--silver)" stroke-width="4">
      <line x1="312" y1="0" x2="312" y2="190"/>
      <line x1="333" y1="0" x2="333" y2="190"/>
      <line x1="355" y1="0" x2="355" y2="190"/>
      <line x1="377" y1="0" x2="377" y2="190"/>
      <line x1="398" y1="0" x2="398" y2="190"/>
    </g>
    <!-- bottom standing lines -->
    <g class="standing-lines" stroke="var(--silver)" stroke-width="4">
      <line x1="845" y1="1052" x2="845" y2="1200"/>
      <line x1="866" y1="1052" x2="866" y2="1200"/>
      <line x1="888" y1="1052" x2="888" y2="1200"/>
      <line x1="910" y1="1052" x2="910" y2="1200"/>
      <line x1="931" y1="1052" x2="931" y2="1200"/>
    </g>
    <!-- title rules -->
    <g class="title-rules" stroke="var(--silver)" stroke-width="4">
      <line x1="584" y1="170" x2="1128" y2="170"/>
      <line x1="584" y1="292" x2="808" y2="292"/>
      <line x1="906" y1="292" x2="1128" y2="292"/>
      <line x1="68" y1="820" x2="612" y2="820"/>
      <line x1="68" y1="942" x2="292" y2="942"/>
      <line x1="390" y1="942" x2="612" y2="942"/>
    </g>
    <!-- product divider -->
    <line class="divider-line" x1="0" y1="556" x2="1200" y2="556" stroke="var(--silver-dark)" stroke-width="3"/>
    <rect class="divider-band" x="0" y="568" width="1200" height="68" fill="url(#band-silver)"/>
  </svg>

  <div class="brand-mark brand-mark--top">VELA</div>

  <div class="title title--top">
    <div class="title__main">
      <span class="title__star">★</span>
      <span class="title__word">LUXE</span>
      <span class="title__star">★</span>
    </div>
    <div class="title__sub">GEL</div>
  </div>
  <div class="coat-name coat-name--top">Top Coat</div>

  <div class="title title--bottom">
    <div class="title__main">
      <span class="title__star">★</span>
      <span class="title__word">LUXE</span>
      <span class="title__star">★</span>
    </div>
    <div class="title__sub">GEL</div>
  </div>
  <div class="coat-name coat-name--bottom">Base Coat</div>

  <div class="brand-mark brand-mark--bottom">VELA</div>
</main>
</body>
</html>
```